Car show marketing A5 one sided leaflet/brochure

We are a car enthusiast group that is hosting a performance vehicle trade show & show and shine event. We require a Brochure/leaflet advertising this trade show . Not folded. Just one sided A5 leaflet. We were liking the look of car headlights (but for the car make/model to be non-descript) just that it is an actual car ... Moody ... there will be a DJ playing and arcade racing etc. so that type of 'electronic' fun, motor enthuiast feel. Plus in the background or somewhere on it have the hall in which we are hosting it. I have attached a photo of the hall. The expo is called "Velocity Harbor Fair" being hosted by "Tamber Motorsport" The catchfrase is "Forging Roadway Kinship" I have also attached the tamber motorsport logo. It will be at the "The Marlowe Pavilion" Brisbane on 9th March 2024 from 9.30am to 5pm. It will be showcasing automotive businesses. Please have somewhere on the brochure there will be live entertainment and kids entertainment. Catering throughout the event. (Food stalls & cafe). Entry just $25 - kids under 12 free. See website for details. www.tambermotorsport.com.au *** I have attached a picture of a idea we had thrown together but obviously we are not in any way able to put together the flyer as we have no experience. We are open for any other design ideas. Thank you!!

Target Market(s)

Car Enthusiasts & families

Industry/Entity Type

Motor

Font styles to use
Serif
Other font styles liked:
• Car racing font such as outrider for example only

Requirements
Must have
• Car feel

```html
<!DOCTYPE html>
<html lang="en">
<head>
<meta charset="utf-8">
<title>Velocity Harbor Fair – Leaflet</title>
<link href="https://fonts.googleapis.com/css2?family=Orbitron:wght@500;600;700&family=Exo+2:ital,wght@1,800;1,900&display=swap" rel="stylesheet">
<style>
  :root {
    --red: #e8332a;
    --red-deep: #b8221a;
    --ink: #1e1b1c;
    --white: #ffffff;
    --mist: #e9eaec;
    --tech: "Orbitron", sans-serif;
    --display: "Exo 2", sans-serif;
  }
  html, body { margin: 0; padding: 0; overflow: hidden; }
  body { width: 846px; height: 1200px; background: var(--white); }
  .leaflet {
    position: relative; width: 846px; height: 1200px; overflow: hidden;
    background: radial-gradient(ellipse at 8% 12%, var(--mist) 0%, var(--white) 45%);
    font-family: var(--tech);
  }
  .abs { position: absolute; }
  .event-when {
    left: 0; width: 846px; top: 62px; margin: 0; text-align: center;
    color: var(--red); font-weight: 600; font-size: 24.5px; line-height: 42px;
    letter-spacing: 1.5px; text-transform: uppercase;
  }
  .hero-photo { left: 0; top: 0; width: 846px; height: 1200px; }
  .tagline-strip {
    left: 40px; top: 456px; width: 770px; height: 44px;
    background: linear-gradient(90deg, rgba(232,51,42,0) 0%, var(--red) 10%, var(--red) 90%, rgba(232,51,42,0) 100%);
    filter: blur(3px);
  }
  .tagline {
    left: 0; width: 846px; top: 456px; margin: 0; text-align: center;
    font-family: var(--display); font-style: italic; font-weight: 900;
    font-size: 31px; line-height: 44px; color: var(--white); letter-spacing: 1px;
    text-transform: uppercase;
  }
  .title-band { background: var(--white); }
  .band-one { left: 0; top: 522px; width: 786px; height: 82px; clip-path: polygon(0 0, 100% 0, 98% 100%, 0 100%); }
  .band-two { left: 225px; top: 611px; width: 621px; height: 71px; clip-path: polygon(1.5% 0, 100% 0, 100% 100%, 0 100%); }
  .title-word {
    margin: 0; font-family: var(--display); font-style: italic; font-weight: 900;
    color: var(--ink); text-transform: uppercase; letter-spacing: -1px;
  }
  .word-one { left: 80px; width: 700px; top: 522px; font-size: 86px; line-height: 82px; text-align: center; }
  .word-two { left: 240px; width: 305px; top: 611px; font-size: 76px; line-height: 71px; text-align: center; }
  .word-box {
    left: 381px; top: 682px; width: 285px; height: 86px; background: var(--red);
    clip-path: polygon(3% 0, 100% 0, 97% 100%, 0 100%);
  }
  .word-three { left: 381px; width: 285px; top: 682px; font-size: 78px; line-height: 86px; text-align: center; }
  .speed-lines { display: block; }
  .extras {
    left: 44px; top: 834px; margin: 0; color: var(--white);
    font-weight: 500; font-size: 21px; line-height: 32px; letter-spacing: 1.5px;
    text-transform: uppercase;
  }
  .entry-panel {
    left: 0; top: 1005px; width: 326px; height: 195px; background: var(--red);
    clip-path: polygon(0 0, 100% 0, 90.5% 100%, 0 100%);
  }
  .entry-text { left: 0; top: 1030px; width: 318px; text-align: center; color: var(--white); }
  .entry-label { margin: 0; font-family: var(--display); font-style: italic; font-weight: 900; font-size: 30px; line-height: 32px; }
  .entry-price { margin: 0; font-family: var(--display); font-style: italic; font-weight: 900; font-size: 70px; line-height: 62px; letter-spacing: 1px; }
  .entry-note { margin: 4px 0 0; font-weight: 500; font-size: 18px; line-height: 25px; letter-spacing: 1.5px; text-transform: uppercase; }
  .hosts { right: 34px; top: 1004px; width: 320px; text-align: right; }
  .hosted-by { margin: 0; color: var(--red); font-weight: 600; font-size: 16px; letter-spacing: 2px; text-transform: uppercase; }
  .host-row { display: flex; justify-content: flex-end; align-items: center; gap: 22px; margin-top: 38px; }
  .host-name { margin: 0; font-weight: 700; font-size: 17px; color: var(--ink); letter-spacing: 1px; text-transform: uppercase; }
  .partner-badge { width: 30px; height: 30px; border-radius: 50%; background: var(--red); }
  .more-info { right: 46px; top: 1112px; margin: 0; color: var(--red); font-weight: 600; font-size: 16px; letter-spacing: 2px; text-transform: uppercase; }
  .site { right: 46px; top: 1143px; margin: 0; color: var(--red); font-weight: 600; font-size: 19px; letter-spacing: 1.2px; text-transform: uppercase; }
</style>
</head>
<body>
<main class="leaflet">
  <svg class="abs hero-photo" viewBox="0 0 846 1200" role="img" aria-label="Moody close-up photograph of a red sports car's headlight and front grille beside a painted striped wall">
    <defs>
      <linearGradient id="carTone" x1="0" y1="0" x2="1" y2="0.3">
        <stop offset="0" stop-color="#d6361f"/>
        <stop offset="0.3" stop-color="#8e1d12"/>
        <stop offset="0.55" stop-color="#c8341e"/>
        <stop offset="0.7" stop-color="#5f6a78"/>
        <stop offset="1" stop-color="#8a8f9c"/>
      </linearGradient>
      <linearGradient id="fade" x1="0" y1="0" x2="0.35" y2="0">
        <stop offset="0" stop-color="#ffffff" stop-opacity="0.55"/>
        <stop offset="1" stop-color="#ffffff" stop-opacity="0"/>
      </linearGradient>
    </defs>
    <path d="M0,215 C300,205 560,165 846,170 L846,890 C760,965 560,1035 330,1050 L0,1045 Z" fill="url(#carTone)"/>
    <path d="M0,215 C300,205 560,165 846,170 L846,890 C760,965 560,1035 330,1050 L0,1045 Z" fill="url(#fade)"/>
  </svg>

  <p class="abs event-when">9th March 2024 from 9.30am to 5pm<br>at "The Marlowe Pavilion" Brisbane</p>

  <div class="abs tagline-strip"></div>
  <p class="abs tagline">Forging Roadway Kinship</p>

  <div class="abs title-band band-one"></div>
  <div class="abs title-band band-two"></div>
  <svg class="abs speed-lines" style="left:0;top:536px" width="58" height="50" viewBox="0 0 58 50">
    <rect x="0" y="0" width="58" height="7" fill="var(--ink)"/>
    <rect x="0" y="20" width="54" height="7" fill="var(--ink)"/>
    <rect x="0" y="40" width="50" height="7" fill="var(--ink)"/>
  </svg>
  <svg class="abs speed-lines" style="left:556px;top:626px" width="290" height="44" viewBox="0 0 290 44">
    <rect x="4" y="0" width="286" height="6" fill="var(--ink)"/>
    <rect x="2" y="18" width="288" height="6" fill="var(--ink)"/>
    <rect x="0" y="36" width="290" height="6" fill="var(--ink)"/>
  </svg>
  <h1 class="abs title-word word-one">Velocity</h1>
  <p class="abs title-word word-two">Harbor</p>
  <div class="abs word-box"></div>
  <p class="abs title-word word-three">Fair</p>

  <p class="abs extras">Live entertainment,<br>kids activities and<br>food available</p>

  <div class="abs entry-panel"></div>
  <div class="abs entry-text">
    <p class="entry-label">ENTRY</p>
    <p class="entry-price">$25</p>
    <p class="entry-note">Free for kids<br>under 12</p>
  </div>

  <div class="abs hosts">
    <p class="hosted-by">Hosted by</p>
    <div class="host-row">
      <p class="host-name">Tamber Motorsport</p>
      <span class="partner-badge" aria-hidden="true"></span>
    </div>
  </div>

  <p class="abs more-info">For more info visit</p>
  <p class="abs site">www.tambermotorsport.com.au</p>
</main>
</body>
</html>
```